Signage for a store*

logo on the two sides of the sign
in the middle is the name of the store witch is VORELT
at the bottom of the two logos, one side for location/address and the other side is contact details phone number is 718-392-6107 address is 2974 THE SIGN WILL BEE 15 FEET BY 4 FEET I WOULD LIKE THAT THE
BACKGROUND OF THE SIGN SHOULD HAVE A NICE COLOR BASE
THAT GOES FOR A WINE STORE

```html
<!DOCTYPE html>
<html lang="en">
<head>
<meta charset="utf-8">
<title>VORELT Store Sign</title>
<link rel="stylesheet" href="https://fonts.googleapis.com/css2?family=Della+Respira&family=Arimo:wght@400&display=swap">
<style>
  :root {
    --wine: #ad1a26;
    --cream: #fdebcb;
    --gold: #c9a03d;
    --page: #ffffff;
  }
  html, body {
    margin: 0;
    padding: 0;
    width: 1200px;
    height: 1000px;
    overflow: hidden;
    background: var(--page);
  }
  .canvas {
    position: relative;
    width: 1200px;
    height: 1000px;
  }
  .sign {
    position: absolute;
    left: 19px;
    top: 345px;
    width: 1162px;
    height: 310px;
    background: var(--wine);
  }
  .side-panel {
    position: absolute;
    top: 6px;
    width: 233px;
    height: 298px;
    background: var(--cream);
    text-align: center;
    color: var(--wine);
  }
  .side-panel--left { left: 6px; }
  .side-panel--right { left: 921px; width: 235px; }
  .brand-mark {
    position: absolute;
    left: 0;
    right: 0;
    top: 40px;
  }
  .brand-dot {
    display: block;
    width: 54px;
    height: 54px;
    margin: 0 auto 12px;
    border-radius: 50%;
    background: var(--gold);
  }
  .brand-name {
    font-family: "Della Respira", serif;
    font-size: 38px;
    letter-spacing: 1px;
    line-height: 1;
    color: var(--wine);
  }
  .panel-info {
    position: absolute;
    left: 0;
    right: 0;
    top: 246px;
    font-family: "Arimo", Arial, sans-serif;
    font-size: 15.5px;
    line-height: 20px;
    margin: 0;
  }
  .store-name {
    position: absolute;
    left: 239px;
    right: 241px;
    top: 88px;
    margin: 0;
    text-align: center;
    font-family: "Della Respira", serif;
    font-weight: 400;
    font-size: 124px;
    line-height: 1;
    letter-spacing: 2px;
    color: var(--cream);
  }
</style>
</head>
<body>
<div class="canvas">
  <div class="sign">
    <div class="side-panel side-panel--left">
      <div class="brand-mark">
        <span class="brand-dot"></span>
        <div class="brand-name">VORELT</div>
      </div>
      <p class="panel-info">2974 Harlow St. Brooklyn<br>N.Y. 11218</p>
    </div>

    <h1 class="store-name">VORELT</h1>

    <div class="side-panel side-panel--right">
      <div class="brand-mark">
        <span class="brand-dot"></span>
        <div class="brand-name">VORELT</div>
      </div>
      <p class="panel-info">Call us on:<br>718-392-6107</p>
    </div>
  </div>
</div>
</body>
</html>
```